依頼詳細
ロゴとのバランス、フォントにこだわりたいです。何パターンかあると決めやすいです。業種、年齢(65歳)的にもシンプルかつラグジュアリー感が希望です。
名刺同様、急募とさせていただきますので、作業が早い方、やり取りがスムーズに進む方を優先させていただく可能性あります。
使用するロゴを添付いたしますが、ロゴのバランスや色については追加・修正しても構いません。
よろしくお願いいたします。
記載項目
ミルカ・ソレイユ株式会社
〒231-0087 神奈川県横浜市栄区桂台西2-18-7-204
TEL045-947-2506 FAX045-947-2507
E-Mail k.moriya@example-mail.jp

```html
<!DOCTYPE html>
<html lang="ja">
<head>
<meta charset="UTF-8">
<title>ミルカ・ソレイユ株式会社 封筒</title>
<link rel="stylesheet" href="https://fonts.googleapis.com/css2?family=Noto+Sans+JP:wght@400;500;700&display=swap">
<style>
  :root {
    --paper: #ffffff;
    --edge: #c9c9c9;
    --postal-red: #d9452b;
    --ink: #1e1e1e;
    --gold: #b8913a;
  }
  * { margin: 0; padding: 0; box-sizing: border-box; }
  html, body { width: 874px; height: 1200px; overflow: hidden; background: var(--paper); }
  .envelope {
    position: relative;
    width: 874px;
    height: 1200px;
    background: var(--paper);
    border: 3px solid var(--edge);
    font-family: "Noto Sans JP", sans-serif;
    color: var(--ink);
  }
  .postal-boxes {
    position: absolute;
    top: 26px;
    left: 446px;
  }
  .sender {
    position: absolute;
    left: 222px;
    top: 1040px;
    display: flex;
    align-items: flex-start;
    gap: 24px;
  }
  .brand-mark {
    width: 92px;
    display: flex;
    flex-direction: column;
    align-items: center;
    gap: 8px;
    padding-top: 8px;
  }
  .brand-square {
    width: 52px;
    height: 52px;
    background: var(--gold);
  }
  .brand-name {
    font-size: 12px;
    font-weight: 700;
    letter-spacing: 0.04em;
    color: var(--ink);
    white-space: nowrap;
  }
  .sender-details { line-height: 1; }
  .company-name {
    font-size: 27px;
    font-weight: 500;
    letter-spacing: 0.06em;
    margin-bottom: 14px;
  }
  .contact-line {
    font-size: 15px;
    font-weight: 400;
    letter-spacing: 0.03em;
    margin-bottom: 6px;
    white-space: nowrap;
  }
  .contact-label { display: inline-block; width: 62px; }
</style>
</head>
<body>
  <div class="envelope">
    <svg class="postal-boxes" width="370" height="52" viewBox="0 0 370 52" aria-hidden="true">
      <g fill="none" stroke="var(--postal-red)" stroke-width="2.5">
        <rect x="1" y="1" width="42" height="50"/>
        <rect x="53" y="1" width="42" height="50"/>
        <rect x="105" y="1" width="42" height="50"/>
        <line x1="153" y1="26" x2="165" y2="26"/>
        <rect x="171" y="3" width="36" height="46"/>
        <rect x="215" y="3" width="36" height="46"/>
        <rect x="259" y="3" width="36" height="46"/>
        <rect x="303" y="3" width="36" height="46"/>
      </g>
    </svg>

    <div class="sender">
      <div class="brand-mark">
        <div class="brand-square"></div>
        <div class="brand-name">MILCA SOLEIL</div>
      </div>
      <div class="sender-details">
        <p class="company-name">ミルカ・ソレイユ株式会社</p>
        <p class="contact-line">〒231-0087</p>
        <p class="contact-line">神奈川県横浜市栄区桂台西2-18-7-204</p>
        <p class="contact-line"><span class="contact-label">TEL：</span>045-612-3879</p>
        <p class="contact-line"><span class="contact-label">FAX：</span>045-612-3880</p>
        <p class="contact-line"><span class="contact-label">E-Mail：</span>k.moriya@example-mail.jp</p>
      </div>
    </div>
  </div>
</body>
</html>
```